Horse-Related Social Media Web Design

Need a social media web design for the world’s largest horse training program, Brindlecott Open Equitation. The site features social media components along with educational material and videos with a free downloadable app for horse owners on-the-go. Although members receive a free 30-day membership, they must choose from three levels of membership when they sign up (similar to kinloreva.com). The original design was based off of glimmerdock.com.

We would like a mash-up of the sign-up page for Chatterlume and Quibbly. The home page will feature an intro video, sign-up field and a tag line and sub text such as:
Ready to Connect?
Connect with your horse, yourself, Brindlecott members and friends you haven’t yet met.

The final design should communicate a hip, trendy site for horse-minded people.

We need the design only, sliced for the website. We will do all coding ourselves.

The current website is www.brindlecottlink.com.

Project Deadline Extended
Reason: We've had multiple designers accept the project, but none have submitted designs.

The deadline of our project has been extended, we have guaranteed it and the budget has been raised to $1,250 US.  

We are looking forward to some excellent submissions!
Thank you.

Please think outside the box. The submissions we've received so far look much like our current site. While we would like a clean, simple look, it should also be trendy and convey that the site is fun without implicitly saying so. We will be tailoring down the text and information on the front page and placing the majority of information inside the information pages in the navigation.

Thank you!

Thank you to everyone who has participated in submitting designs for our contest. 

Target Market(s)

Target market is horse owners and lovers across the world. The company has a very international market with campuses in the UK and Australia and followers literally across the world.

Industry/Entity Type

Training

Requirements
Nice to have
• Please explain why you made certain design choices from a useability perspective when you submit the design.

```html
<!DOCTYPE html>
<html lang="en">
<head>
<meta charset="utf-8">
<title>Brindlecott Connect</title>
<link href="https://fonts.googleapis.com/css2?family=Fira+Sans:wght@400;500;600;700&family=Arimo:wght@400;700&display=swap" rel="stylesheet">
<style>
  :root {
    --sky-blue: #3c5c9e;
    --deep-blue: #0f3682;
    --gold: #c08a32;
    --ember: #6a4a24;
    --badge-blue: #223f93;
    --badge-light: #4a6cbf;
    --badge-yellow: #f7c85a;
    --panel-dark: #1b1c21;
    --panel-mid: #25262c;
    --signup-bg: #3d3f47;
    --field-bg: #55575f;
    --field-line: #8a8c93;
    --text-light: #f2f2f2;
    --text-muted: #c7c8cc;
    --accent-yellow: #f4c13e;
    --tick-green: #6fd636;
    --button-orange: #f0a21a;
    --footer-bg: #262628;
  }
  * { box-sizing: border-box; margin: 0; padding: 0; }
  html, body { width: 1200px; height: 1013px; overflow: hidden; background: var(--panel-dark); }
  body { position: relative; font-family: "Arimo", Arial, sans-serif; color: var(--text-light); }

  .hero {
    position: absolute; left: 0; top: 0; width: 1200px; height: 650px;
    background:
      radial-gradient(ellipse 520px 330px at 640px 330px, rgba(214,158,62,0.95), rgba(150,100,40,0.75) 45%, rgba(60,70,110,0) 100%),
      linear-gradient(180deg, var(--sky-blue) 0%, #2f4f8f 20%, #34406a 45%, var(--ember) 60%, #1a3c7e 85%, var(--deep-blue) 100%);
  }
  .nav-band {
    position: absolute; left: 0; top: 78px; width: 1200px; height: 68px;
    background: rgba(18, 28, 55, 0.55);
    border-top: 1px solid rgba(255,255,255,0.45);
    border-bottom: 1px solid rgba(255,255,255,0.35);
  }
  .main-nav { position: absolute; top: 104px; left: 0; font-family: "Fira Sans", sans-serif; font-weight: 500; font-size: 18px; }
  .main-nav a { position: absolute; color: #fff; text-decoration: none; white-space: nowrap; }

  .member-badge {
    position: absolute; left: 42px; top: 19px; width: 177px; height: 177px;
    border: 5px solid #fff; border-radius: 12px;
    background: linear-gradient(180deg, var(--badge-light) 0%, var(--badge-blue) 45%, #1d3886 100%);
    text-align: center; font-family: "Fira Sans", sans-serif;
  }
  .member-badge .offer { margin-top: 14px; color: var(--badge-yellow); font-weight: 700; font-size: 20px; line-height: 20px; }
  .member-badge .offer-sub { color: #fff; font-weight: 600; font-size: 12px; line-height: 16px; }
  .member-badge .brand { margin-top: 46px; color: var(--badge-yellow); font-weight: 500; font-size: 26px; line-height: 28px; }
  .member-badge .tier { color: var(--badge-yellow); font-weight: 500; font-size: 16px; letter-spacing: 1px; }

  .social-links { position: absolute; top: 25px; left: 1008px; display: flex; gap: 11px; }
  .social-links a {
    display: flex; align-items: center; justify-content: center;
    width: 32px; height: 32px; border-radius: 7px; border: 2px solid #e6e9f0;
    background: #2c4a8a; color: #fff; font-family: "Fira Sans", sans-serif; font-size: 9px; text-decoration: none;
  }

  .member-login { position: absolute; left: 1021px; top: 85px; width: 150px; height: 44px; }
  .member-login .login-btn {
    position: absolute; left: 27px; top: 15px; width: 123px; height: 27px; border-radius: 4px;
    background: linear-gradient(#e4e6ea, #b9bcc3); color: #1d1d1d;
    font-family: "Fira Sans", sans-serif; font-size: 13px; line-height: 27px; padding-left: 16px; word-spacing: 2px;
  }
  .member-login svg { position: absolute; left: 0; top: 0; }

  .content-band { position: absolute; left: 0; top: 650px; width: 1200px; height: 285px; background: var(--panel-dark); }
  .intro-panel { position: absolute; left: 82px; top: 669px; width: 1081px; height: 242px; background: var(--panel-mid); border-radius: 3px; }
  .intro-title { position: absolute; left: 122px; top: 697px; font-size: 23px; color: var(--text-muted); }
  .intro-sub { position: absolute; left: 122px; top: 724px; font-size: 12.5px; color: #e6e6e6; }
  .intro-video { position: absolute; left: 122px; top: 751px; width: 231px; height: 143px; background: #000; }
  .intro-video .controls {
    position: absolute; left: 0; bottom: 0; width: 100%; height: 14px; background: #e9e9e9;
    font-size: 6px; color: #333; line-height: 14px;
  }
  .feature-list { position: absolute; left: 392px; top: 776px; list-style: none; font-size: 13px; color: var(--accent-yellow); }
  .feature-list li { position: relative; padding-left: 27px; height: 17.7px; line-height: 17.7px; }
  .feature-list svg { position: absolute; left: 0; top: -2px; }
  .read-more { position: absolute; left: 622px; top: 859px; font-size: 12px; font-weight: 700; color: #e8e8e8; text-decoration: none; }
  .read-more span { font-weight: 400; margin-left: 6px; }

  .signup-panel { position: absolute; left: 743px; top: 658px; width: 405px; height: 269px; background: var(--signup-bg); border: 1px solid #5b5d66; border-radius: 2px; }
  .signup-panel h2 { position: absolute; left: 67px; top: 19px; font-family: "Fira Sans", sans-serif; font-weight: 500; font-size: 18px; color: #fff; }
  .signup-panel .key-icon { position: absolute; left: 10px; top: 16px; }
  .signup-panel .divider { position: absolute; left: 8px; top: 42px; width: 388px; height: 1px; background: #6b6d75; }
  .signup-field {
    position: absolute; left: 51px; width: 286px; height: 32px; border-radius: 8px;
    background: var(--field-bg); border: 1px solid var(--field-line);
    font-family: "Fira Sans", sans-serif; font-size: 15px; color: #eee; line-height: 30px; padding-left: 46px; word-spacing: 3px;
  }
  .signup-field svg { position: absolute; left: 13px; top: 9px; }
  .field-tick { position: absolute; left: 349px; }
  .btn { position: absolute; top: 239px; height: 35px; border-radius: 18px; font-family: "Fira Sans", sans-serif; font-size: 15px; line-height: 33px; text-align: center; }
  .btn-signup { left: 163px; width: 96px; background: linear-gradient(#ffc23c, #e0850c); border: 1px solid #7a4a00; color: #222; }
  .btn-clear { left: 263px; width: 79px; background: linear-gradient(#55575e, #2c2d32); border: 1px solid #15161a; color: #d5d5d5; }

  .site-footer {
    position: absolute; left: 0; top: 935px; width: 1200px; height: 78px;
    background: repeating-linear-gradient(45deg, #2a2a2c 0 2px, var(--footer-bg) 2px 4px);
    text-align: center; font-size: 13px; color: #e4e4e4;
  }
  .site-footer .copyright { margin-top: 22px; letter-spacing: 0.3px; }
  .site-footer .legal { margin-top: 6px; }
  .site-footer .legal a { color: #e4e4e4; text-decoration: none; margin: 0 5px; }
</style>
</head>
<body>
  <div class="hero" role="img" aria-label="Photograph of a herd of horses galloping through golden backlit dust at sunset"></div>
  <div class="nav-band"></div>

  <nav class="main-nav">
    <a href="#" style="left:285px">Home</a>
    <a href="#" style="left:375px">Features</a>
    <a href="#" style="left:488px">Pricing</a>
    <a href="#" style="left:585px">Buzz</a>
    <a href="#" style="left:665px">FAQs</a>
    <a href="#" style="left:743px">Giving Back</a>
  </nav>

  <div class="member-badge">
    <div class="offer">FREE 30 DAY</div>
    <div class="offer-sub">TRIAL MEMBERSHIP!</div>
    <div class="brand">Brindlecott</div>
    <div class="tier">MEMBER</div>
  </div>

  <div class="social-links">
    <a href="#" aria-label="Quibbly">Qb</a>
    <a href="#" aria-label="Chatterlume">Ch</a>
    <a href="#" aria-label="Proflink">Pl</a>
    <a href="#" aria-label="Inkpost">Ip</a>
  </div>

  <div class="member-login">
    <svg width="40" height="44" viewBox="0 0 40 44" aria-hidden="true">
      <circle cx="12" cy="10" r="7" fill="#6b4a3a"/>
      <path d="M1 30 q11 -14 22 0 z" fill="#c44a6a"/>
      <circle cx="20" cy="20" r="7" fill="#d9a77c"/>
      <path d="M8 42 q12 -18 24 0 z" fill="#2f8fd8"/>
    </svg>
    <div class="login-btn">Member Login</div>
  </div>

  <div class="content-band"></div>
  <div class="intro-panel"></div>
  <h1 class="intro-title">Welcome to Brindlecott Connect</h1>
  <p class="intro-sub">Horse Training Tools &amp; Community Support</p>

  <div class="intro-video">
    <svg width="231" height="129" viewBox="0 0 231 129" aria-hidden="true">
      <path d="M108 53 l10 6 l-10 6 z" fill="#fff"/>
    </svg>
    <div class="controls">&nbsp;&#9654;&nbsp; 00:00 ─────────────────────────── 00:00</div>
  </div>

  <ul class="feature-list">
    <li><svg width="18" height="18" viewBox="0 0 18 18"><path d="M2 9 l5 5 l9 -12" stroke="var(--tick-green)" stroke-width="3" fill="none"/></svg>Part Social Network</li>
    <li><svg width="18" height="18" viewBox="0 0 18 18"><path d="M2 9 l5 5 l9 -12" stroke="var(--tick-green)" stroke-width="3" fill="none"/></svg>Part Personal Trainer Part Personal Trainer</li>
    <li><svg width="18" height="18" viewBox="0 0 18 18"><path d="M2 9 l5 5 l9 -12" stroke="var(--tick-green)" stroke-width="3" fill="none"/></svg>Part Digital Diary Part Digital Diary</li>
    <li><svg width="18" height="18" viewBox="0 0 18 18"><path d="M2 9 l5 5 l9 -12" stroke="var(--tick-green)" stroke-width="3" fill="none"/></svg>Brindlecott Connect is fun! Brindlecott Connect is fun!</li>
  </ul>
  <a class="read-more" href="#">Read More<span>&gt;&gt;</span></a>

  <section class="signup-panel">
    <svg class="key-icon" width="50" height="36" viewBox="0 0 50 36" aria-hidden="true">
      <ellipse cx="30" cy="14" rx="17" ry="8" fill="#2a8ee0"/>
      <circle cx="11" cy="12" r="8" fill="none" stroke="#e6e6e6" stroke-width="3"/>
      <path d="M11 20 v14 M11 28 h5" stroke="#e6e6e6" stroke-width="3"/>
    </svg>
    <h2>SIGN UP</h2>
    <div class="divider"></div>

    <div class="signup-field" style="top:59px"><svg width="16" height="12" viewBox="0 0 16 12"><rect x="0.5" y="0.5" width="15" height="11" fill="none" stroke="#ccc"/><path d="M0.5 0.5 l7.5 6 l7.5 -6" fill="none" stroke="#ccc"/></svg>Email</div>
    <div class="signup-field" style="top:102px"><svg width="16" height="12" viewBox="0 0 16 12"><rect x="0.5" y="0.5" width="15" height="11" fill="none" stroke="#ccc"/><path d="M0.5 0.5 l7.5 6 l7.5 -6" fill="none" stroke="#ccc"/></svg>Email Confirmation</div>
    <div class="signup-field" style="top:146px"><svg width="12" height="13" viewBox="0 0 12 13"><path d="M3 6 v-2 a3 3 0 0 1 6 0 v2" fill="none" stroke="#ccc" stroke-width="1.6"/><rect x="1" y="6" width="10" height="7" fill="#ccc"/></svg>Password</div>
    <div class="signup-field" style="top:190px"><svg width="12" height="13" viewBox="0 0 12 13"><path d="M3 6 v-2 a3 3 0 0 1 6 0 v2" fill="none" stroke="#ccc" stroke-width="1.6"/><rect x="1" y="6" width="10" height="7" fill="#ccc"/></svg>Password Confirmation</div>

    <svg class="field-tick" style="top:55px" width="26" height="24" viewBox="0 0 26 24"><path d="M3 12 l7 7 l13 -17" stroke="var(--tick-green)" stroke-width="4" fill="none"/></svg>
    <svg class="field-tick" style="top:97px" width="26" height="24" viewBox="0 0 26 24"><path d="M3 12 l7 7 l13 -17" stroke="var(--tick-green)" stroke-width="4" fill="none"/></svg>
    <svg class="field-tick" style="top:139px" width="26" height="24" viewBox="0 0 26 24"><path d="M3 12 l7 7 l13 -17" stroke="var(--tick-green)" stroke-width="4" fill="none"/></svg>
    <svg class="field-tick" style="top:183px" width="26" height="24" viewBox="0 0 26 24"><path d="M3 12 l7 7 l13 -17" stroke="var(--tick-green)" stroke-width="4" fill="none"/></svg>

    <div class="btn btn-signup">Sign Up</div>
    <div class="btn btn-clear">Clear</div>
  </section>

  <footer class="site-footer">
    <p class="copyright">© Copyright 2012 Brindlecott Open Equitation, Inc. All Rights Reserved.</p>
    <p class="legal"><a href="#">Terms and Conditions of Service</a><a href="#">Privacy Policy</a></p>
  </footer>
</body>
</html>
```